Automotive eCommerce Business looking for a business card design

Looking for a clean and simple business card design. Our company name is "Harbor Crest Auto" and we are a company specializing in the ecommerce sales of automotive parts, specifically for pick up trucks and large SUVs. Our company colours are red, black, and white.

Feel free to use the logo provided or create a new logo that you seem fit. Looking forward to your creative ideas!

Industry/Entity Type

Automotive

Contact Information for Business Card

We were thinking of a possibly two-sided design featuring just the logo and company name on one side, and personal information on the other side. Single sided designs will be considered as well.

Font styles to use
Serif
Sans Serif
Decorative

Colors
ec1f27
ffffff
000000

Requirements
Must have
• Space for employee's name, title, phone number and email address, along with the company address and website somewhere.

```html
<!DOCTYPE html>
<html lang="en">
<head>
<meta charset="utf-8">
<title>Harbor Crest Auto – Business Card</title>
<link href="https://fonts.googleapis.com/css2?family=Open+Sans:wght@400;600;700&family=Raleway:wght@600;700&display=swap" rel="stylesheet">
<style>
  :root {
    --stage: #0b0b0b;
    --card-white: #ffffff;
    --brand-red: #a51e23;
    --text-red: #a3171d;
    --ink: #111111;
    --body-ink: #1c1c1c;
  }
  * { margin: 0; padding: 0; box-sizing: border-box; }
  html, body {
    width: 1200px;
    height: 900px;
    overflow: hidden;
    background: var(--stage);
  }
  .canvas {
    position: relative;
    width: 1200px;
    height: 900px;
  }
  .card {
    position: absolute;
    top: 307px;
    width: 437px;
    height: 270px;
    border-radius: 10px;
    overflow: hidden;
  }
  .card-front {
    left: 150px;
    background: var(--card-white);
  }
  .card-back {
    left: 609px;
    background: var(--brand-red);
  }
  .brand-block {
    position: absolute;
    left: 20px;
    top: 68px;
    width: 212px;
    text-align: center;
  }
  .brand-dot {
    display: block;
    width: 80px;
    height: 80px;
    margin: 0 auto 22px;
    border-radius: 50%;
    background: var(--brand-red);
  }
  .brand-name {
    font-family: "Raleway", sans-serif;
    font-weight: 700;
    font-size: 18px;
    color: var(--ink);
    white-space: nowrap;
  }
  .divider {
    position: absolute;
    left: 240px;
    top: 74px;
    width: 1px;
    height: 121px;
    background: var(--brand-red);
  }
  .contact-block {
    position: absolute;
    left: 257px;
    top: 69px;
    font-family: "Open Sans", sans-serif;
    color: var(--body-ink);
  }
  .person-name {
    font-size: 14.5px;
    font-weight: 700;
    color: var(--text-red);
    line-height: 18px;
    letter-spacing: 0.1px;
  }
  .person-title {
    font-size: 11.5px;
    line-height: 15px;
    margin-bottom: 9px;
  }
  .contact-list { list-style: none; }
  .contact-item {
    display: flex;
    align-items: center;
    gap: 6px;
    font-size: 11.5px;
    line-height: 16px;
  }
  .contact-icon { width: 8px; height: 8px; flex: none; }
  .address {
    margin-top: 7px;
    font-size: 11.5px;
    line-height: 15.5px;
  }
  .back-field {
    position: absolute;
    inset: 0;
    background: var(--brand-red);
  }
  .back-name {
    position: absolute;
    left: 0;
    right: 0;
    top: 165px;
    text-align: center;
    font-family: "Raleway", sans-serif;
    font-weight: 700;
    font-size: 15px;
    color: var(--card-white);
  }
</style>
</head>
<body>
<main class="canvas">
  <section class="card card-front" aria-label="Business card front">
    <div class="brand-block">
      <span class="brand-dot"></span>
      <p class="brand-name">Harbor Crest Auto Ltd</p>
    </div>
    <div class="divider"></div>
    <div class="contact-block">
      <p class="person-name">DANIEL REYES</p>
      <p class="person-title">Managing Director</p>
      <ul class="contact-list">
        <li class="contact-item">
          <svg class="contact-icon" viewBox="0 0 10 10"><path fill="#a3171d" d="M2 0.5 L3.8 2.6 L2.8 3.8 Q4 6.2 6.2 7.2 L7.4 6.2 L9.5 8 L8.2 9.5 Q4.5 9.5 2 6.5 Q0 4 0.5 1.8 Z"/></svg>
          (044)987654321
        </li>
        <li class="contact-item">
          <svg class="contact-icon" viewBox="0 0 10 10"><rect x="0.5" y="2" width="9" height="6.5" fill="#a3171d"/><path d="M0.8 2.3 L5 5.6 L9.2 2.3" stroke="#fff" stroke-width="0.9" fill="none"/></svg>
          info@harborcrestauto.com
        </li>
        <li class="contact-item">
          <svg class="contact-icon" viewBox="0 0 10 10"><circle cx="5" cy="5" r="4.6" fill="#a3171d"/><path d="M2 3.5 Q3.5 3 4 4.5 Q3 6 4.5 8 M6 2 Q6.5 4 8 4.5" stroke="#fff" stroke-width="0.9" fill="none"/></svg>
          www.harborcrestauto.com
        </li>
      </ul>
      <p class="address">5678, Harbor Lane,<br>Bayview City, 54321</p>
    </div>
  </section>

  <section class="card card-back" aria-label="Business card back">
    <div class="back-field" role="img" aria-label="Red field with a faint repeating brand pattern"></div>
    <p class="back-name">Harbor Crest Auto</p>
  </section>
</main>
</body>
</html>
```